Billboard Design for Equipment Rental Business

We need a billboard design for our equipment rental business called Brindlewood Equipment Company. We are based in Georgia. We rent construction tools, equipment, and dumpsters. We currently have a design but feel like we could get something better. Our phone number is 912-730-2591 and our website is www.brindlewoodequipment-example.com

```html
<!DOCTYPE html>
<html lang="en">
<head>
<meta charset="utf-8">
<title>Brindlewood Equipment Company – Billboard</title>
<link rel="stylesheet" href="https://fonts.googleapis.com/css2?family=Archivo:wdth,wght@125,900&family=Montserrat:wght@500;600&family=Oswald:wght@700&display=swap">
<style>
  :root {
    --sign-yellow: #f8bb17;
    --ink: #0c0f10;
    --paper: #ffffff;
    --backdrop: #d4d4d4;
  }
  * { box-sizing: border-box; margin: 0; padding: 0; }
  html, body {
    width: 910px;
    height: 1200px;
    overflow: hidden;
    background: var(--backdrop);
  }
  .canvas {
    width: 910px;
    height: 1200px;
    display: flex;
    align-items: center;
    justify-content: center;
  }
  .billboard {
    position: relative;
    width: 840px;
    height: 410px;
    background: var(--sign-yellow);
    box-shadow: 2px 3px 6px rgba(0,0,0,0.3);
    overflow: hidden;
  }
  .brand {
    position: absolute;
    top: 0; left: 0; right: 0;
    height: 200px;
    display: flex;
    align-items: center;
    justify-content: center;
    gap: 22px;
  }
  .brand-mark {
    width: 58px;
    height: 58px;
    background: var(--ink);
  }
  .brand-name {
    font-family: "Oswald", sans-serif;
    font-weight: 700;
    color: var(--ink);
    line-height: 1;
    text-transform: uppercase;
  }
  .brand-name .primary {
    display: block;
    font-size: 68px;
    letter-spacing: 1px;
  }
  .brand-name .secondary {
    display: block;
    font-size: 25px;
    letter-spacing: 2.4px;
    margin-top: 8px;
  }
  .service-band {
    position: absolute;
    top: 240px;
    left: 0; right: 0;
    height: 110px;
    background: var(--paper);
  }
  .service-tab {
    position: absolute;
    top: 203px;
    left: 50px;
    width: 748px;
    height: 57px;
    background: var(--ink);
    border-radius: 26px 26px 0 26px;
    display: flex;
    align-items: center;
    justify-content: center;
    font-family: "Montserrat", sans-serif;
    font-weight: 500;
    font-size: 29px;
    color: var(--sign-yellow);
    letter-spacing: 0.3px;
    white-space: nowrap;
  }
  .service-tab .dot {
    display: inline-block;
    width: 10px;
    height: 10px;
    border-radius: 50%;
    background: var(--sign-yellow);
    margin: 0 12px 0 14px;
    vertical-align: middle;
  }
  .phone {
    position: absolute;
    top: 262px;
    left: 0; right: 0;
    text-align: center;
    font-family: "Archivo", sans-serif;
    font-weight: 900;
    font-stretch: 125%;
    font-size: 70px;
    line-height: 80px;
    color: var(--ink);
    letter-spacing: 1px;
  }
  .website {
    position: absolute;
    top: 350px;
    left: 0; right: 0;
    height: 60px;
    display: flex;
    align-items: center;
    justify-content: center;
    font-family: "Montserrat", sans-serif;
    font-weight: 600;
    font-size: 30px;
    color: var(--ink);
    letter-spacing: 0.5px;
  }
</style>
</head>
<body>
  <main class="canvas">
    <section class="billboard" aria-label="Brindlewood Equipment Company billboard">
      <header class="brand">
        <div class="brand-mark" aria-hidden="true"></div>
        <h1 class="brand-name">
          <span class="primary">Brindlewood</span>
          <span class="secondary">Equipment Company</span>
        </h1>
      </header>
      <div class="service-band"></div>
      <p class="service-tab">
        <span class="dot"></span>EQUIPMENT<span class="dot"></span>TOOLS<span class="dot"></span>DUMPSTERS
      </p>
      <p class="phone">912-730-2591</p>
      <p class="website">www.brindlewoodequipment-example.com</p>
    </section>
  </main>
</body>
</html>
```